Vélra, a Gourmet and Medicinal Mushroom company in Egypt, is looking for packaging design.

We need a packaging design for our 150-200grams fresh mushroom trays. These are gourmet mushrooms, completely new to the Egyptian market.
Attached is our logo, brand guidelines, the package material and dimensions, and a similar packaging idea that inspired us (but we want ours to stand out more and have more information).
Our trays are made of corrugated cardboard, and we will use the tray on the left side of attached images, but with the top opening design of the right side tray ( a big window at the top of the tray to allow consumers to see the product inside). (LxWxH = 17cm x 12cm x 8cm)
The tray will have printed (1 color) information that is shared amongst all types of mushrooms (company name, printed labels of Organic/Non-GMO/Vegan/Environmental/Recyclable) then we will add sticker labels to each tray for the information of the different products we have (mushroom name, QR code to link a recipe from our website, unique flavor or benefits, nutritional value, shelf life)
We have 7 SKU's of different mushroom types. We only need one design for the tray and labels, and we will interchange the text to match the various SKU's.
- King Oyster (200 grams)
- Lion's Mane (200 grams)
- Shiitake (200 grams)
- Enoki (150 grams)
- White Shimeji (150 grams)
- Brown Shimeji (150 grams)
- Chestnut (200 grams)

The tray must have a cutout openings either on the sides or the front or back for airing out the moisture (these must be narrow or thin cutouts to prevent insect from getting in, please avoid circles, etc). The top will be a large window opening with a plastic film for protection.
More information to follow.

```html
<!DOCTYPE html>
<html lang="en">
<head>
<meta charset="utf-8">
<title>Vélra Fresh – Tray Dieline and Labels</title>
<link rel="stylesheet" href="https://fonts.googleapis.com/css2?family=Oswald:wght@400;700&family=Amaranth:ital,wght@1,700&family=Open+Sans:wght@400&display=swap">
<style>
  :root {
    --kraft: #d8b784;
    --kraft-light: #dcbd8c;
    --cut: #ff1a1a;
    --fold: #19ff19;
    --ink: #92503c;
    --white: #ffffff;
    --black: #111111;
    --label-green: #8ea228;
    --label-red: #ec3138;
    --label-orange: #f48836;
    --label-brown: #924f3c;
    --leaf-tint: rgba(232, 70, 60, 0.13);
  }
  html, body {
    margin: 0;
    padding: 0;
    overflow: hidden;
    background: var(--kraft);
  }
  .canvas {
    width: 1200px;
    height: 561px;
    overflow: hidden;
    background: linear-gradient(180deg, #e2c69a 0%, var(--kraft) 6%, var(--kraft-light) 100%);
  }
  .artwork { display: block; width: 1200px; height: 561px; }
  .cut-line { fill: none; stroke: var(--cut); stroke-width: 5; stroke-linejoin: miter; }
  .fold-line { fill: none; stroke: var(--fold); stroke-width: 9; }
  .fold-line--thin { stroke-width: 4; }
  .brand-name { font-family: "Oswald", sans-serif; font-weight: 700; text-anchor: middle; }
  .brand-tag { font-family: "Oswald", sans-serif; font-weight: 400; text-anchor: middle; letter-spacing: 6px; }
  .label-product { font-family: "Amaranth", sans-serif; font-style: italic; font-weight: 700; fill: var(--white); text-anchor: middle; font-size: 34px; }
  .label-weight { font-family: "Open Sans", sans-serif; fill: var(--white); text-anchor: middle; font-size: 20px; }
  .panel-address { font-family: "Open Sans", sans-serif; fill: var(--ink); font-size: 20px; text-anchor: middle; }
  .cert-badge { fill: none; stroke: var(--ink); stroke-width: 3; }
  .leaf-motif { fill: var(--leaf-tint); }
</style>
</head>
<body>
<div class="canvas">
<svg class="artwork" viewBox="0 0 2576 1204" preserveAspectRatio="none" xmlns="http://www.w3.org/2000/svg">

  <!-- Product sticker labels -->
  <g class="sticker-label">
    <rect x="47" y="62" width="249" height="322" fill="var(--label-green)"/>
    <text class="brand-name" x="172" y="160" font-size="52" fill="var(--black)">Vélra</text>
    <text class="brand-tag" x="172" y="182" font-size="12" fill="var(--black)">FRESH</text>
    <text class="label-product" x="172" y="258">King Oyster</text>
    <text class="label-weight" x="172" y="358">200 gm</text>
  </g>
  <g class="sticker-label">
    <rect x="305" y="62" width="250" height="322" fill="var(--label-red)"/>
    <text class="brand-name" x="432" y="162" font-size="56" fill="var(--white)">Vélra</text>
    <text class="brand-tag" x="432" y="186" font-size="12" fill="var(--white)">FRESH</text>
    <text class="label-product" x="436" y="258">Lion's Mane</text>
    <text class="label-weight" x="432" y="358">200 gm</text>
  </g>
  <g class="sticker-label">
    <rect x="576" y="59" width="250" height="323" fill="var(--label-orange)"/>
    <text class="brand-name" x="704" y="160" font-size="56" fill="var(--white)">Vélra</text>
    <text class="brand-tag" x="704" y="184" font-size="12" fill="var(--white)">FRESH</text>
    <text class="label-product" x="707" y="256">Lion's Mane</text>
    <text class="label-weight" x="703" y="356">200 gm</text>
  </g>
  <g class="sticker-label">
    <rect x="842" y="59" width="249" height="323" fill="var(--label-brown)"/>
    <text class="brand-name" x="969" y="160" font-size="56" fill="var(--white)">Vélra</text>
    <text class="brand-tag" x="969" y="184" font-size="12" fill="var(--white)">FRESH</text>
    <text class="label-product" x="973" y="256">Lion's Mane</text>
    <text class="label-weight" x="968" y="356">200 gm</text>
  </g>

  <!-- Tray dieline: cut lines -->
  <g class="dieline-cuts">
    <polyline class="cut-line" points="248,580 172,600 172,858 248,880"/>
    <line class="cut-line" x1="248" y1="580" x2="884" y2="580"/>
    <polyline class="cut-line" points="880,580 878,540 893,523 912,452 1326,452"/>
    <line class="cut-line" x1="1326" y1="580" x2="1326" y2="140"/>
    <path class="cut-line" d="M1372,138 L1326,135 L1326,92 Q1326,68 1350,68 L1932,68 Q1956,68 1956,92 L1956,135 L1910,138"/>
    <line class="cut-line" x1="1956" y1="140" x2="1956" y2="580"/>
    <rect class="cut-line" x="1410" y="245" width="470" height="235" rx="62"/>
    <polyline class="cut-line" points="1962,580 1962,445 2356,445 2373,520 2392,540 2392,580"/>
    <line class="cut-line" x1="2392" y1="580" x2="2392" y2="878"/>
    <polyline class="cut-line" points="250,880 250,1133 424,1133 408,1071 720,1071 705,1133 878,1133 878,880"/>
    <polyline class="cut-line" points="884,884 1128,1033 1112,1096 1322,1096 1322,884"/>
    <path class="cut-line" d="M1326,884 L1478,1070 L1478,1120 Q1478,1133 1492,1133 L1778,1133 Q1792,1133 1792,1120 L1792,1070 L1948,884"/>
    <polyline class="cut-line" points="1948,884 1948,1096 2228,1096 2212,1033 2400,878"/>
  </g>

  <!-- Tray dieline: fold lines -->
  <g class="dieline-folds">
    <rect class="fold-line" x="250" y="582" width="630" height="296"/>
    <rect class="fold-line" x="880" y="582" width="444" height="296"/>
    <rect class="fold-line" x="1324" y="582" width="630" height="296"/>
    <line class="fold-line fold-line--thin" x1="1962" y1="580" x2="2392" y2="580"/>
    <line class="fold-line fold-line--thin" x1="1954" y1="878" x2="2398" y2="878"/>
    <line class="fold-line fold-line--thin" x1="1376" y1="140" x2="1910" y2="140"/>
  </g>

  <!-- Long side panels: leaf motif areas -->
  <rect class="leaf-motif" x="285" y="648" width="555" height="162" rx="40" role="img" aria-label="Outlined leaf sprig pattern printed in red"/>
  <rect class="leaf-motif" x="1372" y="645" width="555" height="162" rx="40" role="img" aria-label="Outlined leaf sprig pattern printed in red"/>

  <!-- Short end panel: brand and certificates -->
  <g class="end-panel">
    <text class="brand-name" x="1104" y="742" font-size="104" fill="var(--ink)">Vélra</text>
    <text class="brand-tag" x="1106" y="775" font-size="24" fill="var(--ink)">FRESH</text>
    <circle class="cert-badge" cx="1000" cy="825" r="16"/>
    <circle class="cert-badge" cx="1048" cy="820" r="14"/>
    <circle class="cert-badge" cx="1094" cy="820" r="13"/>
    <circle class="cert-badge" cx="1141" cy="820" r="13"/>
    <circle class="cert-badge" cx="1189" cy="820" r="13"/>
  </g>

  <!-- Short end panel: brand and address -->
  <g class="end-panel">
    <text class="brand-name" x="2173" y="735" font-size="104" fill="var(--ink)">Vélra</text>
    <text class="brand-tag" x="2175" y="769" font-size="24" fill="var(--ink)">FRESH</text>
    <text class="panel-address" x="2128" y="822">address etc</text>
    <text class="panel-address" x="2128" y="841">address etc</text>
    <text class="panel-address" x="2252" y="822">address etc</text>
    <text class="panel-address" x="2252" y="841">address etc</text>
  </g>
</svg>
</div>
</body>
</html>
```